2 menu designs: Tarn Hospitality

I have 2 restaurants that are going though large menu changes. I wanted them to have a style change as well!
-one is a steakhouse menu: must fit in two portrait legal pages. there is a picture of the menu book attached. The emphasis of the menu should be on the "steaks" and "prime rib". attached are menu items that need to be included
-the other is a burger restaurant: must fit on one legal landscape page. The focus of this menu should go to the middle of the page and emphasis "burgers" and "fries". attached is the general layout I'm interested in and the menu items that need to be included. Logo for restaurant is also included. picture of restaurant included

Both must be able to be edited often but the number of items and general placement of these items will not change

Industry/Entity Type

Hospitality

```html
<!DOCTYPE html>
<html lang="en">
<head>
<meta charset="utf-8">
<title>Tarnside Menu</title>
<link href="https://fonts.googleapis.com/css2?family=Lobster&family=Oswald:wght@400;500;600&family=Roboto+Condensed:wght@400;500&family=Poiret+One&display=swap" rel="stylesheet">
<style>
:root{
  --stage:#e9e9e6;
  --orange:#f07a26;
  --orange-light:#f9a14a;
  --red:#d4281f;
  --badge-red:#e8261c;
  --gold:#f3b33d;
  --cream:#f7f1dc;
  --ink:#1e1a17;
  --rule:#f0a49a;
  --paper:#ffffff;
}
*{box-sizing:border-box;margin:0;padding:0}
html,body{width:1200px;height:1000px;overflow:hidden}
body{background:var(--stage);position:relative;font-family:"Roboto Condensed",sans-serif;color:var(--ink)}
.page{position:absolute;top:28px;width:545px;height:897px;background:var(--paper);box-shadow:3px 4px 8px rgba(0,0,0,.35);overflow:hidden}
.page--left{left:28px}
.page--right{left:630px}
.page__header{height:87px;background:linear-gradient(90deg,var(--orange),var(--orange-light) 50%,var(--orange));display:flex;align-items:center;justify-content:center}
.page__footer{position:absolute;bottom:0;left:0;right:0;height:17px;background:linear-gradient(90deg,var(--orange),var(--orange-light) 50%,var(--orange))}
.brand{font-family:"Oswald",sans-serif;font-weight:600;font-size:36px;letter-spacing:1px;color:var(--red);display:flex;align-items:center;gap:10px;padding-top:10px}
.brand__dot{width:10px;height:10px;border-radius:50%;background:var(--red)}
.heading{font-family:"Lobster",sans-serif;color:var(--red);text-shadow:1px 2px 2px rgba(0,0,0,.25);display:flex;align-items:center;justify-content:center;gap:8px;white-space:nowrap;line-height:1.1}
.col-beginnings{position:absolute;left:0;top:87px;width:235px;bottom:17px;background:linear-gradient(90deg,var(--cream),#fffef8);border-right:2px solid var(--rule);padding:14px 14px 0 30px}
.col-beginnings .heading{font-size:31px;justify-content:flex-start;margin-bottom:16px}
.item{margin-bottom:12px;line-height:1.2}
.item__name{font-family:"Oswald",sans-serif;font-weight:500;font-size:11.5px;text-transform:uppercase}
.item__price{font-family:"Oswald",sans-serif;font-size:10px;font-weight:400}
.item__desc{font-size:9.5px}
.badge{background:var(--badge-red);box-shadow:3px 4px 5px rgba(0,0,0,.45);text-align:center;color:var(--gold);font-family:"Oswald",sans-serif;text-transform:uppercase;line-height:1.05}
.badge--popover{position:absolute;left:31px;top:690px;width:168px;height:92px;padding-top:9px;font-size:15px}
.badge__strong{font-family:"Lobster",sans-serif;text-transform:none;color:#fff;font-size:20px}
.badge__shadowed{color:#f6d07a;letter-spacing:1px;font-weight:600}
.col-plat{position:absolute;left:237px;right:0;top:87px;padding-top:12px;text-align:center}
.col-plat .heading{font-size:29px;margin-bottom:6px}
.day{margin-bottom:10px}
.day__name{font-family:"Poiret One",sans-serif;font-size:22px;color:#555;line-height:1.15}
.day__dish{font-family:"Oswald",sans-serif;font-weight:500;font-size:11.5px}
.day__desc{font-size:9.5px;padding:0 20px}
.kids{position:absolute;left:300px;top:628px;width:230px}
.kids .heading{font-size:31px;justify-content:flex-start;margin-left:56px}
.kids__price{font-family:"Oswald",sans-serif;font-size:10px;color:var(--ink);text-shadow:none;align-self:flex-start;margin-top:6px}
.kids__note{font-size:9.5px;margin:4px 0 2px}
.kids__note--lg{font-size:11px;margin-bottom:6px}
.kids__item{font-family:"Oswald",sans-serif;font-weight:500;font-size:11.5px;margin-bottom:3px;text-transform:uppercase}
.kids__foot{font-family:"Oswald",sans-serif;font-size:11.5px;text-transform:uppercase;line-height:1.3}
.prime{position:absolute;left:95px;top:99px;width:362px;height:160px;border:2px solid var(--rule);background:linear-gradient(180deg,#f4eed2,#fffdf4);text-align:center;padding-top:8px}
.prime .heading{font-size:28px}
.prime__sub{font-family:"Poiret One",sans-serif;font-size:15px;font-weight:bold}
.prime__desc{font-family:"Oswald",sans-serif;font-size:9.5px;line-height:1.7;text-transform:uppercase}
.prime__cuts{display:flex;justify-content:center;gap:40px;margin-top:12px;font-family:"Oswald",sans-serif;font-size:11.5px;font-weight:500}
.prime__cuts small{font-weight:400;font-size:9.5px}
.prime__cuts div div{font-size:9.5px;font-weight:400;margin-top:5px}
.broiler{position:absolute;left:0;right:0;top:270px;text-align:center}
.broiler .heading{font-size:28px;margin-bottom:8px}
.broiler__intro{font-size:9.5px;line-height:1.25;text-transform:uppercase;margin-bottom:3px}
.steak{margin-bottom:4px;line-height:1.2}
.steak__name{font-family:"Oswald",sans-serif;font-weight:500;font-size:11.5px;text-transform:uppercase}
.steak__price{font-size:9.5px}
.mark{color:var(--red)}
.broiler__key{font-size:9.5px;color:var(--red)}
.badge--side{position:absolute;width:126px;height:69px;padding-top:6px;font-size:14px;font-weight:400}
.badge--rubs{left:32px;top:360px}
.badge--addons{left:387px;top:360px}
.badge__white{color:#fff;font-family:"Oswald",sans-serif;font-weight:600;font-size:11px;letter-spacing:1.5px;text-transform:none}
.section{position:absolute;left:0;right:0}
.section .heading{font-size:28px;margin-bottom:6px}
.section--entrees{top:504px}
.section--sides{top:678px}
.two-col{display:flex;padding:0 30px 0 46px;gap:12px;text-align:center}
.two-col > div{flex:1}
.two-col .steak{margin-bottom:6px}
.section--sides .two-col .steak{margin-bottom:8px}
.two-col .steak__price{font-size:9.5px}
</style>
</head>
<body>

<section class="page page--left">
  <header class="page__header"><div class="brand"><span class="brand__dot"></span>Tarnside</div></header>

  <div class="col-beginnings">
    <h2 class="heading">Beginnings</h2>
    <div class="item"><div class="item__name">Shrimp Louie <span class="item__price">$18</span></div><div class="item__desc">Baby Gem Lettuce, Avocado, Little Deviled Egg</div></div>
    <div class="item"><div class="item__name">Lamb Ribs <span class="item__price">$16</span></div><div class="item__desc">Chimichurri, Herbed Riatta, Feta</div></div>
    <div class="item"><div class="item__name">Seasonal Soup <span class="item__price">MP</span></div><div class="item__desc">Market's Best, Seasonal Garnish</div></div>
    <div class="item"><div class="item__name">Mixed Baby Lettuces <span class="item__price">$9</span></div><div class="item__desc">Shaved Market Vegetables, Lemon Herb Vinaigrette</div></div>
    <div class="item"><div class="item__name">Heirloom Tomatoes <span class="item__price">$12</span></div><div class="item__desc">Buratta Cheese, Basil Essence, Red Wine Vinaigrette</div></div>
    <div class="item"><div class="item__name">Roasted Beets <span class="item__price">$8</span></div><div class="item__desc">Soft Goat Cheese, Pistachio, Citrus Vinaigrette</div></div>
    <div class="item"><div class="item__name">Steakhouse Wedge <span class="item__price">$8</span></div><div class="item__desc">Double Cut Bacon, Market Tomato,<br>Coastal Blue Cheese Dressing</div></div>
    <div class="item"><div class="item__name">Baby Kale Caesar <span class="item__price">$9</span></div><div class="item__desc">Baby Kale, Romaine Hearts, Parmesan, Garlic Brown Butter Crouton, Artichoke Caesar Vinaigrette</div></div>
    <div class="item"><div class="item__name">West Coast Oysters <span class="item__price">$18</span></div><div class="item__desc">Seasonal Mignonette</div></div>
    <div class="item"><div class="item__name">Spiced Poached Shrimp <span class="item__price">$12</span></div><div class="item__desc">Classic Cocktail, Green Goddess Dressing</div></div>
    <div class="item"><div class="item__name">Double Cute Bacon <span class="item__price">$8</span></div><div class="item__desc">Applewood Smoked, Strap Molasses BBQ</div></div>
    <div class="item"><div class="item__name">Spinach Artichoke Fondue <span class="item__price">$8</span></div><div class="item__desc">Sourdough Crouton, Harbor Spice Chips</div></div>
  </div>

  <div class="badge badge--popover">Marco's<br><span class="badge__shadowed">Famous</span><br><span class="badge__strong">Pop-Over</span><br>Complimentary</div>

  <div class="col-plat">
    <h2 class="heading">Plat du Jour</h2>
    <div class="day"><div class="day__name">Sunday</div><div class="day__dish">BEEF SHORT RIB</div><div class="day__desc">24 Hour Braise, Root Vegetable Hash, Burgundy Reduction</div></div>
    <div class="day"><div class="day__name">Monday</div><div class="day__dish">NORTH BEACH CIOPPINO</div><div class="day__desc">Shellfish And Spiced Tomato Broth, Crab Toast</div></div>
    <div class="day"><div class="day__name">Tuesday</div><div class="day__dish">SONOMA LAMB T-BONE</div><div class="day__desc">Roasted Eggplant Caponata, Lamb Jus</div></div>
    <div class="day"><div class="day__name">Wednesday</div><div class="day__dish">COQ AU VIN</div><div class="day__desc">Herb Roasted Breast, Red Wine Braised Thigh, Potato Puree, Root Vegetables</div></div>
    <div class="day"><div class="day__name">Thursday</div><div class="day__dish">DAY BOAT SCALLOPS</div><div class="day__desc">Cast Iron Seared, Creamed Sweetcorn, Herbed Lemon Citronette</div></div>
    <div class="day"><div class="day__name">Friday</div><div class="day__dish">BEEF SHORT RIB</div><div class="day__desc">24 Hour Braise, Root Vegetable Hash, Burgundy Reduction</div></div>
    <div class="day"><div class="day__name">Saturday</div><div class="day__dish">NORTH BEACH CIOPPINO</div><div class="day__desc">Shellfish And Spiced Tomato Broth, Crab Toast</div></div>
  </div>

  <div class="kids">
    <h2 class="heading">Kids <span class="kids__price">$6.95</span></h2>
    <p class="kids__note">Served with Entrée | Dessert | Drink</p>
    <p class="kids__note kids__note--lg">Kids under 10 EAT FREE before 7pm –<br><span style="font-size:9.5px">up to 2 kids per each purchased adult entree</span></p>
    <div class="kids__item">Chicken Tenders</div>
    <div class="kids__item">Burger</div>
    <div class="kids__item">Steak</div>
    <div class="kids__item">Salmon</div>
    <div class="kids__item">Mac &amp; Cheese</div>
    <div class="kids__item">Seasonal Mixed Vegetables</div>
    <div class="kids__foot">Choice of Fries or Broccoli<br>&amp; Ice Cream Sundae or Fruit</div>
  </div>

  <div class="page__footer"></div>
</section>

<section class="page page--right">
  <header class="page__header"><div class="brand"><span class="brand__dot"></span>Tarnside</div></header>

  <div class="prime">
    <h2 class="heading">Prime Rib</h2>
    <p class="prime__sub">Featuring Heritage Reserve Beef</p>
    <p class="prime__desc">Signature spice rubbed, all day roasted, served with<br>our baby iceberg wedge and loaded salt baked potato</p>
    <div class="prime__cuts">
      <div>QUEEN CUT <small>14oz</small><div>$28.95</div></div>
      <div>PRINCESS CUT <small>9oz</small><div>$22.95</div></div>
    </div>
  </div>

  <div class="broiler">
    <h2 class="heading">From the Broiler</h2>
    <p class="broiler__intro">Our Angus steaks are served a la carte<br>with our sea salt &amp; crushed peppercorn rub,</p>
    <div class="steak"><div class="steak__name">Steak Frites au Poivre</div><div class="steak__price">6oz $19.95 <span class="mark">HRB</span></div></div>
    <div class="steak"><div class="steak__name">NY Strip</div><div class="steak__price">16oz $38.95 <span class="mark">HRB</span></div></div>
    <div class="steak"><div class="steak__name">Center Cut Filet</div><div class="steak__price">8oz $30.95 | 12oz $34.95</div></div>
    <div class="steak"><div class="steak__name">Rib Eye</div><div class="steak__price">16oz $33.95 <span class="mark">HRB</span></div></div>
    <p class="broiler__key">HRB = Featuring Heritage Reserve Beef</p>
  </div>

  <div class="badge badge--side badge--rubs">Rubs<br>&amp; Sauces<br><span class="badge__white">Peppercorn<br>Red Wine</span></div>
  <div class="badge badge--side badge--addons">Signature<br>Add-Ons<br><span class="badge__white">Lobster<br>Shrimp</span></div>

  <div class="section section--entrees">
    <h2 class="heading">Entrées</h2>
    <div class="two-col">
      <div>
        <div class="steak"><div class="steak__name">Seared Pacific Salmon <span class="steak__price">$24</span></div><div class="steak__price">Grain Mustard Bearnaise, Seasonal Succotash</div></div>
        <div class="steak"><div class="steak__name">Vegetable Mixed Grill <span class="steak__price">$15</span></div><div class="steak__price">Basil Balsamic, Herbed Goat Cheese Crepe</div></div>
        <div class="steak"><div class="steak__name">Petaluma Brick Chicken <span class="steak__price">$19</span></div><div class="steak__price">Baby Carrot And Pea Tendril Salad, Roast Chicken Jus</div></div>
      </div>
      <div>
        <div class="steak"><div class="steak__name">Tarnside Frisco Melt</div><div class="steak__price">Hand Pressed Patty, Grilled Sourdough, White Cheddar, Caramelized Onion, Not So Secret Sauce,</div></div>
        <div class="steak"><div class="steak__name">Steakhouse Burger</div><div class="steak__price">Hand Pressed Patty, Brioche Bun, Lettuce,<br>Tomato, Onion</div></div>
        <div class="steak"><div class="steak__name">Double Cut Pork Chop <span class="steak__price">$21</span></div><div class="steak__price">Creamed Cipolini, Pork Jus</div></div>
      </div>
    </div>
  </div>

  <div class="section section--sides">
    <h2 class="heading">Seasonal Sides</h2>
    <div class="two-col">
      <div>
        <div class="steak"><div class="steak__name">Creamed Spinach <span class="steak__price">$6</span></div><div class="steak__price">Bacon Shallot Crumble</div></div>
        <div class="steak"><div class="steak__name">Black Truffle Mac &amp; Cheese <span class="steak__price">$8</span></div><div class="steak__price">Micro Broccoli</div></div>
        <div class="steak"><div class="steak__name">Steamed Asparagus <span class="steak__price">$7</span></div><div class="steak__price">Garlic Streusel, Lemon Vinaigrette</div></div>
        <div class="steak"><div class="steak__name">Roasted Mushrooms <span class="steak__price">$6</span></div><div class="steak__price">Onion Thyme Jus</div></div>
      </div>
      <div>
        <div class="steak"><div class="steak__name">Horseradish or Classic Whipped<br>Potatoes <span class="steak__price">$6</span></div><div class="steak__price">Creamery Butter</div></div>
        <div class="steak"><div class="steak__name">Salt Baked Potato <span class="steak__price">$6</span></div><div class="steak__price">White Cheddar Fondue, Scallions, Smoked Bacon</div></div>
        <div class="steak"><div class="steak__name">Duck Fat Fries <span class="steak__price">$6</span></div><div class="steak__price">Sea Salt, Cracked Pepper</div></div>
        <div class="steak"><div class="steak__name">Market Best <span class="steak__price">$6</span></div><div class="steak__price">Farm To Table, Changes Daily</div></div>
      </div>
    </div>
  </div>

  <div class="page__footer"></div>
</section>

</body>
</html>
```